Mortgage Broking boutique Business

I’m wanting a revamped look to my existing business card design. I do like the black and silver but happy to have other colours introduced based on your creation. I’ve attached a copy of my current card so you can have a starting point updated details noted brloe. I deal with high net worth individuals so need my card to be sophisticated, classy that gives off a classy vibe

Target Market(s)

High net worth, wealthy

Industry/Entity Type

Mortgage Brokerage

Contact Information for Business Card

Job title: Finance Executive
Phone: +61 7 3287 4419
Mobile: 0471 352 608
Email: marcus@quillbrookcapital.com.au
Web: www.quillbrookcapital.com.au
Address: level 36 Tindale Court, 58 Harwick St Brisbane QLD 4000

Font styles to use
Other font styles liked:
• Helvetica

Colors

Designer to choose colors to be used in the design.

Requirements
Must have
• Use my existing card design as a starting point

```html
<!DOCTYPE html>
<html lang="en">
<head>
<meta charset="utf-8">
<title>Quillbrook Capital — Business Card</title>
<link href="https://fonts.googleapis.com/css2?family=Inter:wght@300;400&display=swap" rel="stylesheet">
<style>
  :root {
    --page: #ffffff;
    --card-edge: #050505;
    --card-glow: #2e2d2f;
    --stitch: #6e6e70;
    --silver: #e4e4e6;
    --silver-soft: #c9c9cc;
  }
  * { margin: 0; padding: 0; box-sizing: border-box; }
  html, body {
    width: 1200px; height: 900px; overflow: hidden;
    background: var(--page);
    font-family: "Inter", "Helvetica Neue", Arial, sans-serif;
  }
  .canvas { position: relative; width: 1200px; height: 900px; }
  .card {
    position: absolute; left: 348px; width: 545px; height: 310px;
    border-radius: 22px;
    background: radial-gradient(ellipse 45% 60% at 50% 50%, var(--card-glow) 0%, #141414 60%, var(--card-edge) 100%);
    color: var(--silver);
    text-align: center;
  }
  .card--front { top: 90px; }
  .card--back { top: 467px; }
  .card__stitch {
    position: absolute; left: 19px; right: 18px; top: 16px; bottom: 16px;
    border: 3px dotted var(--stitch);
    border-radius: 16px;
  }
  .brand {
    position: absolute; left: 0; right: 0; top: 123px;
  }
  .brand__name {
    font-weight: 300; font-size: 31px; letter-spacing: 5px; line-height: 1;
    padding-left: 5px;
  }
  .brand__sub {
    margin-top: 6px;
    font-weight: 400; font-size: 14px; letter-spacing: 2.5px; color: var(--silver-soft);
    padding-left: 2px;
  }
  .back__domain {
    position: absolute; left: 0; right: 0; top: 47px;
    font-weight: 300; font-size: 26px; line-height: 1;
  }
  .person { position: absolute; left: 0; right: 0; top: 101px; }
  .person__name { font-size: 18px; font-weight: 400; line-height: 1.1; }
  .person__title { font-size: 14px; font-weight: 300; color: var(--silver-soft); margin-top: 2px; }
  .contact {
    position: absolute; left: 0; right: 0; top: 169px;
    font-size: 13px; font-weight: 300; line-height: 16.5px; color: var(--silver-soft);
  }
  .contact__sep { display: inline-block; margin: 0 6px; color: var(--silver); font-weight: 400; }
</style>
</head>
<body>
<main class="canvas">
  <section class="card card--front" aria-label="Card front">
    <div class="card__stitch"></div>
    <div class="brand">
      <div class="brand__name">QUILLBROOK</div>
      <div class="brand__sub">CAPITAL</div>
    </div>
  </section>

  <section class="card card--back" aria-label="Card back">
    <div class="card__stitch"></div>
    <div class="back__domain">QUILLBROOK.CAPITAL</div>
    <div class="person">
      <div class="person__name">MARCUS LELAND</div>
      <div class="person__title">Finance Executive</div>
    </div>
    <address class="contact" style="font-style: normal;">
      P: +61 7 3287 4419<span class="contact__sep">|</span>M: 0471 352 608<br>
      E: marcus@quillbrookcapital.com.au<br>
      W: www.quillbrookcapital.com.au<br>
      A: level 36 Tindale Court, 58 Harwick<br>
      St Brisbane QLD 4000
    </address>
  </section>
</main>
</body>
</html>
```